Website for business behind new health app called Tormix

A pelvic health app pre-launch website (tormix.app), with a primary focus on signing up users to the beta tester wait list for when the app is ready. As such, the main hero image/section on the home page should include a CTA for sign up above the fold.

Two types of users, healthcare practitioners and general users (the practitioners’ patients or any other patient).

The website’s aesthetic shall follow simple/elegant styling, with client inspiration noted as the following:
The clean, modern and practical feel of https://quillnest.com but with the illustration choices and style of www.varuto.org.au - That is, a focus on app feature screenshots (when ready) in a mockup format (preferably in an actual hand like on varuto) and simple line style representative icons. We want it to be as simple as possible for ease of user experience and clarity.

On clicking the CTA sign up buttons, the user will be directed to a sign up form, details on the sitemap page. All sign up forms completed should be emailed to client’s email inbox directly.

Please advise any plugins you want to use especially if paid licenses are required. For forms Lumen Sheets or Brisk Panels are good. Cobblery is fine but please specify license cost.

The brand aesthetic is one of calming/relaxing pastel greens and some blues. See Word doc for color guides.

Typography is outlined attached Word Doc.

Sitemap also in Word Doc

Pages include:
Home
Features
About

```html
<!DOCTYPE html>
<html lang="en">
<head>
<meta charset="utf-8">
<title>Tormix — Pelvic Health App</title>
<link href="https://fonts.googleapis.com/css2?family=Roboto+Slab:wght@300;400&family=Poppins:wght@400;500;600&display=swap" rel="stylesheet">
<style>
:root{
  --green:#7b9f84;
  --green-dark:#5f8669;
  --mint:#e4f0e8;
  --mint-soft:#eef5f0;
  --slate:#8c92ae;
  --ink:#1f1f1f;
  --text:#444;
  --muted:#777;
  --line:#dcdcdc;
  --gray-bg:#f1f1f1;
  --star:#f2b41c;
}
*{margin:0;padding:0;box-sizing:border-box}
html,body{width:1200px;height:5021px;overflow:hidden;background:#fff}
body{position:relative;font-family:"Poppins",sans-serif;color:var(--text)}
.abs{position:absolute}
.serif{font-family:"Roboto Slab",serif;font-weight:300;color:var(--ink)}
.btn{position:absolute;display:flex;align-items:center;justify-content:center;gap:8px;border-radius:30px;color:#fff;font-size:12px;font-weight:500;text-transform:uppercase;letter-spacing:.3px}
.btn-green{background:var(--green)}
.btn-slate{background:var(--slate)}
.btn-sq{border-radius:5px}
.logo{position:absolute;display:flex;align-items:center;gap:10px;font-size:36px;font-weight:500;color:var(--green)}
.logo .dot{width:26px;height:26px;border-radius:50%;background:var(--green)}
/* header */
.nav a{position:absolute;top:40px;font-size:13px;color:var(--ink);text-decoration:none}
/* hero */
.hero{top:100px;left:0;width:1200px;height:600px;background:var(--gray-bg);overflow:hidden}
.hero-visual{position:absolute;left:560px;top:0;width:640px;height:560px;background:linear-gradient(120deg,#eeeeee 0%,#f3e6e2 45%,#e9d3cf 70%,#f5f5f5 100%)}
.hero h1{position:absolute;left:148px;top:88px;font-size:52px;line-height:55px}
.hero p{position:absolute;left:148px;top:285px;font-size:21px;line-height:32px;color:var(--ink)}
.dots span{position:absolute;width:10px;height:10px;border-radius:50%;border:1px solid #777}
/* split sections */
.circle-art{position:absolute;border-radius:50%;background:var(--mint)}
.split h2{position:absolute;font-size:42px;line-height:46px}
.split p{position:absolute;font-size:13.5px;line-height:28.5px;color:var(--text);width:425px}
.underline{position:absolute;height:2px;background:var(--green)}
/* features */
.band{position:absolute;left:0;width:1200px;background:var(--mint)}
.feat-title{font-size:16px;font-weight:500;color:var(--ink);font-size:14px}
.feat{position:absolute;width:250px}
.feat p{font-size:11px;line-height:20px;color:var(--text);margin-top:4px}
.feat.left{text-align:right}
.ficon{position:absolute;width:54px;height:54px;border-radius:50%;background:#fff;display:flex;align-items:center;justify-content:center}
.phone{position:absolute;left:527px;top:1817px;width:143px;height:308px;border-radius:20px;background:#111;padding:6px}
.phone .screen{width:100%;height:100%;border-radius:15px;background:radial-gradient(ellipse at 50% 60%,#c8592a 0%,#3b1a12 40%,#0c0c0c 75%)}
/* testimonials */
.card{position:absolute;top:2500px;width:292px;height:270px;background:#fff;border-radius:8px;box-shadow:0 6px 24px rgba(0,0,0,.08);text-align:center}
.card h4{margin-top:80px;font-size:14px;font-weight:600;color:var(--ink)}
.card .role{font-size:10px;color:var(--muted);margin-top:3px}
.card .stars{color:var(--star);font-size:13px;letter-spacing:2px;margin-top:6px}
.card p{font-size:11.5px;line-height:22px;margin:12px 24px 0;color:var(--text)}
.card .q{font-family:"Roboto Slab",serif;color:#b9cfbf;font-size:26px;margin-top:8px}
.avatar{position:absolute;top:2460px;width:80px;height:80px;border-radius:50%}
/* ecosystem */
.eco-item{position:absolute;top:3122px;width:140px;text-align:center;font-size:12.5px;color:#666}
.eco-item svg{display:block;margin:0 auto 8px}
.video{position:absolute;left:130px;top:3245px;width:938px;height:380px;background:#fff;border-radius:8px;overflow:hidden}
/* clients */
.clients{position:absolute;left:137px;top:3905px;width:925px;height:490px;display:grid;grid-template-columns:repeat(4,1fr);grid-template-rows:repeat(4,1fr)}
.clients div{display:flex;align-items:center;justify-content:center;gap:8px;font-size:27px;font-weight:500;color:var(--ink);border-right:1px solid var(--line);border-bottom:1px solid var(--line)}
.clients div:nth-child(4n){border-right:none}
.clients div:nth-child(n+13){border-bottom:none}
.clients i{display:inline-block;width:24px;height:24px;border-radius:50%}
/* footer */
.footer{position:absolute;left:0;top:4470px;width:1200px;height:520px;background:#f2f2f2}
.fcol h5{font-family:"Roboto Slab",serif;font-weight:400;font-size:17px;color:var(--ink)}
.fcol ul{list-style:none;margin-top:22px}
.fcol li{font-size:14px;color:var(--ink);margin-bottom:24px;display:flex;align-items:center;gap:10px}
.fcol li::before{content:"";width:5px;height:5px;border-radius:50%;background:#e8a86b}
.social li::before{display:none}
.social .sq{width:28px;height:28px;border-radius:6px;background:#e2e2e2}
.copy{position:absolute;left:0;top:4990px;width:1200px;height:31px;background:var(--slate);color:#fff;font-size:11.5px;display:flex;align-items:center;justify-content:center}
</style>
</head>
<body>

<!-- Header -->
<div class="logo" style="left:145px;top:24px">Tormix<span class="dot"></span></div>
<nav class="nav">
  <a style="left:512px">Home</a>
  <a style="left:583px">Features ⌄</a>
  <a style="left:683px">About ⌄</a>
</nav>
<div class="btn btn-green" style="left:778px;top:23px;width:150px;height:50px">➤ Try Tormix!</div>
<div class="btn btn-slate" style="left:935px;top:23px;width:124px;height:50px">→ Sign Up</div>

<!-- Hero -->
<section class="hero abs">
  <div class="hero-visual" role="img" aria-label="Anatomical pelvic model on a desk beside a clinician writing notes"></div>
  <h1 class="serif">Empowering Your<br>Pelvic Health<br>Journey</h1>
  <p>Join the Waitlist for Our Innovative<br>Pelvic Floor App</p>
  <div class="btn btn-green" style="left:148px;top:387px;width:276px;height:58px;font-size:13px">➤ Sign Up For Beta Access</div>
  <div class="dots">
    <span style="left:576px;top:438px"></span>
    <span style="left:594px;top:438px;background:#333;border-color:#333"></span>
    <span style="left:612px;top:438px"></span>
  </div>
  <svg class="abs" style="left:0;top:470px" width="1200" height="130" viewBox="0 0 1200 130">
    <path d="M0 50 C200 150 420 30 620 70 C820 110 980 140 1200 80 L1200 130 L0 130Z" fill="#fff"/>
    <path d="M0 40 C180 110 350 70 520 60 C700 50 850 100 1200 60" stroke="#9db9a3" stroke-width="10" fill="none"/>
    <path d="M430 110 C650 40 900 150 1200 95" stroke="#cfe0d4" stroke-width="8" fill="none"/>
  </svg>
</section>

<!-- Healthcare Practitioners -->
<section class="split">
  <div class="circle-art" style="left:172px;top:790px;width:383px;height:383px" role="img" aria-label="Illustration of three healthcare practitioners reviewing a clipboard"></div>
  <h2 class="serif" style="left:610px;top:822px">Healthcare<br>Practitioners</h2>
  <p style="left:610px;top:938px">Lorem Ipsum is simply dummy text of the printing atypesetting industry. Lorem Ipsum has been the industry's standard dummy text ever since the when an unknown printer took galley of type and scrambled it to make a type specimen book.</p>
  <div class="btn btn-green btn-sq" style="left:610px;top:1078px;width:120px;height:42px;font-size:11px">Read More</div>

  <h2 class="serif" style="left:173px;top:1228px">General Users</h2>
  <p style="left:173px;top:1298px">Lorem Ipsum is simply dummy text of the printing atypesetting industry. Lorem Ipsum has been the industry's standard dummy text ever since the when an unknown printer took galley of type and scrambled it to make a type specimen book.</p>
  <div class="btn btn-green btn-sq" style="left:173px;top:1439px;width:120px;height:42px;font-size:11px">Read More</div>
  <div class="circle-art" style="left:645px;top:1180px;width:383px;height:383px" role="img" aria-label="Illustration of three women standing together"></div>
</section>

<!-- Features -->
<section class="band" style="top:1645px;height:630px"></section>
<h2 class="serif abs" style="left:0;width:1200px;top:1718px;text-align:center;font-size:42px">Features Our Patients Have Requested</h2>
<div class="underline" style="left:560px;top:1772px;width:80px"></div>

<svg class="abs" style="left:480px;top:1900px" width="240" height="130">
  <line x1="0" y1="5" x2="50" y2="5" stroke="#999"/><line x1="190" y1="5" x2="240" y2="5" stroke="#999"/>
  <line x1="0" y1="127" x2="50" y2="127" stroke="#999"/><line x1="190" y1="127" x2="240" y2="127" stroke="#999"/>
</svg>
<div class="phone"><div class="screen" role="img" aria-label="App screen showing a glowing pelvis visual with the Tormix name and a download button"></div></div>

<div class="feat left" style="left:157px;top:1874px"><div class="feat-title">Educational Resources</div><p>Lorem Ipsum Is Simply Dummy Text Of The Printing And Typesetting Industry</p></div>
<div class="ficon" style="left:420px;top:1878px"><svg width="26" height="26" viewBox="0 0 26 26" fill="none" stroke="#5f8669" stroke-width="1.6"><rect x="5" y="3" width="14" height="19" rx="2"/><line x1="9" y1="8" x2="15" y2="8"/><line x1="9" y1="12" x2="15" y2="12"/><line x1="9" y1="16" x2="13" y2="16"/></svg></div>
<div class="feat left" style="left:153px;top:1998px"><div class="feat-title">Symptom Tracker</div><p>Lorem Ipsum Is Simply Dummy Text Of The Printing And Typesetting Industry</p></div>
<div class="ficon" style="left:420px;top:2000px"><svg width="26" height="26" viewBox="0 0 26 26" fill="none" stroke="#5f8669" stroke-width="1.6"><circle cx="11" cy="14" r="7"/><line x1="16" y1="19" x2="22" y2="24"/><path d="M8 4h6"/></svg></div>

<div class="ficon" style="left:721px;top:1878px"><svg width="26" height="26" viewBox="0 0 26 26" fill="none" stroke="#5f8669" stroke-width="1.6"><rect x="3" y="5" width="20" height="17" rx="2"/><line x1="3" y1="10" x2="23" y2="10"/><line x1="8" y1="2" x2="8" y2="7"/><line x1="18" y1="2" x2="18" y2="7"/></svg></div>
<div class="feat" style="left:790px;top:1878px"><div class="feat-title">Appointment Reminders</div><p>Lorem Ipsum Is Simply Dummy Text Of The Printing And Typesetting Industry</p></div>
<div class="ficon" style="left:721px;top:2003px"><svg width="26" height="26" viewBox="0 0 26 26" fill="none" stroke="#5f8669" stroke-width="1.6"><circle cx="13" cy="5" r="3"/><path d="M13 8v8M7 12h12M13 16l-4 7M13 16l4 7"/></svg></div>
<div class="feat" style="left:790px;top:2004px"><div class="feat-title">Exercise Programs</div><p>Lorem Ipsum Is Simply Dummy Text Of The Printing And Typesetting Industry</p></div>

<div class="btn btn-green btn-sq" style="left:503px;top:2152px;width:193px;height:40px;font-size:11px">Sign Up For Beta Access</div>

<!-- Testimonials -->
<h2 class="serif abs" style="left:0;width:1200px;top:2340px;text-align:center;font-size:42px">See What Our Patients Says</h2>
<div class="underline" style="left:560px;top:2395px;width:80px"></div>

<div class="card" style="left:140px"><h4>Mara Olsen</h4><div class="role">Lorem Ipsum Is Simply</div><div class="stars">★★★★★</div><p>Lorem Ipsum Is Simply Dummy Texprintinty Pesettindustry. Lorem Ipsum Has Been The Induststan Dummy Text Ever Since The 1500s,</p><div class="q">❞</div></div>
<div class="card" style="left:455px"><h4>Lena Brooks</h4><div class="role">Lorem Ipsum Is Simply</div><div class="stars">★★★★★</div><p>Lorem Ipsum Is Simply Dummy Texprintinty Pesettindustry. Lorem Ipsum Has Been The Induststan Dummy Text Ever Since The 1500s,</p><div class="q">❞</div></div>
<div class="card" style="left:768px"><h4>Iris Kovac</h4><div class="role">Lorem Ipsum Is Simply</div><div class="stars">★★★★★</div><p>Lorem Ipsum Is Simply Dummy Texprintinty Pesettindustry. Lorem Ipsum Has Been The Induststan Dummy Text Ever Since The 1500s,</p><div class="q">❞</div></div>
<div class="avatar" style="left:246px;background:linear-gradient(#e9d9c4,#c9b091)" role="img" aria-label="Portrait photo of a patient"></div>
<div class="avatar" style="left:561px;background:linear-gradient(#6a8fa4,#d4a33b)" role="img" aria-label="Portrait photo of a patient"></div>
<div class="avatar" style="left:874px;background:linear-gradient(#f2c7d3,#5a3a34)" role="img" aria-label="Portrait photo of a patient"></div>

<svg class="abs" style="left:550px;top:2835px" width="100" height="24">
  <circle cx="8" cy="12" r="2" fill="#888"/><circle cx="28" cy="12" r="2" fill="#888"/>
  <circle cx="50" cy="12" r="7" fill="none" stroke="#555"/><circle cx="50" cy="12" r="3" fill="#555"/>
  <circle cx="72" cy="12" r="2" fill="#888"/><circle cx="92" cy="12" r="2" fill="#888"/>
</svg>

<!-- Ecosystem -->
<section class="band" style="top:2922px;height:788px;background:linear-gradient(180deg,#e3efe7,#e8f1eb 60%,#dde9e1)"></section>
<h2 class="serif abs" style="left:0;width:1200px;top:2990px;text-align:center;font-size:40px">Explore the ecosystem and benefits of Tormix</h2>
<p class="abs" style="left:0;width:1200px;top:3058px;text-align:center;font-size:12.5px;color:#888">Lorem Ipsum has been the industry's standard dummy text since the 1500s</p>

<div class="eco-item" style="left:95px"><svg width="40" height="46" viewBox="0 0 40 46" fill="none" stroke="#6f9479" stroke-width="1.8"><circle cx="22" cy="9" r="6"/><path d="M16 18c-6 6-6 16 0 20l10 4M22 20c8 2 10 12 4 18"/></svg>Pregnancy</div>
<div class="eco-item" style="left:273px"><svg width="46" height="46" viewBox="0 0 46 46" fill="none" stroke="#6f9479" stroke-width="1.8"><path d="M8 8c0 10 6 12 6 20s4 12 9 12 9-4 9-12 6-10 6-20"/><path d="M14 20h18"/></svg>Bowel Disorder</div>
<div class="eco-item" style="left:460px"><svg width="46" height="46" viewBox="0 0 46 46" fill="none" stroke="#6f9479" stroke-width="1.8"><circle cx="18" cy="22" r="9"/><circle cx="28" cy="22" r="9"/><path d="M18 31v10M13 37h10M34 16l7-7M36 9h5v5"/></svg>Sexual Health</div>
<div class="eco-item" style="left:630px"><svg width="46" height="46" viewBox="0 0 46 46" fill="none" stroke="#6f9479" stroke-width="1.8"><path d="M6 10c4 0 8 4 10 10M40 10c-4 0-8 4-10 10M10 24c0 10 6 16 13 16s13-6 13-16"/><circle cx="23" cy="28" r="5"/></svg>Pelvic Pain</div>
<div class="eco-item" style="left:797px"><svg width="40" height="46" viewBox="0 0 40 46" fill="none" stroke="#6f9479" stroke-width="1.8"><circle cx="20" cy="9" r="6"/><path d="M10 42V26c0-6 4-10 10-10s10 4 10 10v16"/><circle cx="20" cy="30" r="5"/></svg>Postpartum</div>
<div class="eco-item" style="left:958px"><svg width="46" height="46" viewBox="0 0 46 46" fill="none" stroke="#6f9479" stroke-width="1.8"><path d="M6 12c6-4 10 2 12 6h10c2-4 6-10 12-6M18 18c0 8 2 14 5 18 3-4 5-10 5-18"/><circle cx="6" cy="12" r="3"/><circle cx="40" cy="12" r="3"/></svg>Menopause</div>

<div class="video">
  <div class="abs" style="left:0;top:0;width:300px;height:380px;background:linear-gradient(110deg,#d7d7d7,#eeeeee 60%,#fff)" role="img" aria-label="Faded anatomical illustration of the pelvic region"></div>
  <svg class="abs" style="left:428px;top:150px" width="80" height="80"><circle cx="40" cy="40" r="40" fill="#8faf97"/><path d="M32 26l22 14-22 14z" fill="#fff"/></svg>
</div>

<!-- Clients -->
<h2 class="serif abs" style="left:0;width:1200px;top:3812px;text-align:center;font-size:42px">See Our Clientele Section</h2>
<div class="clients">
  <div><i style="background:#f2a33a"></i>brightly</div>
  <div><i style="background:#55a06a"></i>TERRAN</div>
  <div><i style="background:#2f9a9a"></i>Scriptory</div>
  <div><i style="background:#e2543a"></i>swiftway</div>
  <div><i style="background:#222"></i>orbita</div>
  <div><i style="background:#e0492d"></i>VULPEX</div>
  <div><i style="background:#f0614a"></i>tunely</div>
  <div><i style="background:#d8495d"></i>boardly</div>
  <div><i style="background:#f2a33a"></i>NORDHAVEN</div>
  <div><i style="background:#d6292a"></i>KELMORA</div>
  <div><i style="background:#3aa0c8"></i>lumio</div>
  <div><i style="background:#8a3fb0"></i>zenta</div>
  <div><i style="background:#f0a52a"></i>cellix</div>
  <div><i style="background:#f2a33a"></i>aurelis</div>
  <div><i style="background:#e0457b"></i>petalo</div>
  <div><i style="background:#e0234c"></i>sunward</div>
</div>

<!-- Footer -->
<svg class="abs" style="left:0;top:4440px" width="1200" height="140" viewBox="0 0 1200 140">
  <path d="M0 30 C250 90 500 10 750 50 C950 80 1080 40 1200 60 L1200 140 L0 140Z" fill="#f2f2f2"/>
  <path d="M0 25 C220 70 420 20 620 40 C820 60 980 120 1200 50" stroke="#9db9a3" stroke-width="9" fill="none"/>
  <path d="M300 80 C600 20 900 110 1200 70" stroke="#cfe0d4" stroke-width="7" fill="none"/>
</svg>
<footer class="footer">
  <div class="logo" style="left:148px;top:180px">Tormix<span class="dot"></span></div>
  <svg class="abs" style="left:148px;top:274px" width="16" height="20" viewBox="0 0 16 20" fill="none" stroke="#8faf97" stroke-width="1.8"><path d="M8 19s6-7 6-11a6 6 0 0 0-12 0c0 4 6 11 6 11z"/><circle cx="8" cy="8" r="2"/></svg>
  <p class="abs" style="left:182px;top:270px;font-size:14px;line-height:26px;color:var(--ink)">418 Fernway Ct. Millbrook<br>Oregon 97310</p>
  <svg class="abs" style="left:148px;top:330px" width="18" height="18" viewBox="0 0 24 24" fill="none" stroke="#8faf97" stroke-width="2"><path d="M5 3h4l2 5-3 2a12 12 0 0 0 6 6l2-3 5 2v4a2 2 0 0 1-2 2A17 17 0 0 1 3 5a2 2 0 0 1 2-2z"/></svg>
  <p class="abs" style="left:182px;top:330px;font-size:14px;color:var(--ink)">Phone: +100 555 0147</p>
  <div class="btn btn-green" style="left:133px;top:398px;width:125px;height:42px;font-size:10px">➤ Try Tormix!</div>
  <div class="btn btn-slate" style="left:268px;top:398px;width:108px;height:42px;font-size:10px">→ Sign Up</div>

  <div class="fcol abs" style="left:445px;top:188px"><h5>Information</h5><ul><li>Home</li><li>Features</li><li>About Us</li><li>Career</li><li>Contact Us</li></ul></div>
  <div class="fcol abs" style="left:670px;top:188px"><h5>Customer Service</h5><ul><li>Shipping &amp; Returns</li><li>Contact Us</li><li>Terms Of Service</li><li>Sitemap</li><li>Support</li></ul></div>
  <div class="fcol social abs" style="left:925px;top:188px"><h5>Social Media</h5><ul><li><span class="sq"></span>Chatterly</li><li><span class="sq"></span>Snapnest</li><li><span class="sq"></span>Worklane</li><li><span class="sq"></span>Viewbox</li></ul></div>
</footer>
<div class="copy">© 2024 Tormix. All Right Reserved</div>

</body>
</html>
```